Qolvar Energy Information Site Redesign

Re-vamp current site at qolvarenergy.com to include new logo, verbiage updates as needed, redesign, etc. Company overview and additional information on current QVR url.

```html
<!DOCTYPE html>
<html lang="en">
<head>
<meta charset="utf-8">
<title>Qolvar Energy Information</title>
<link href="https://fonts.googleapis.com/css2?family=Ubuntu:wght@400;500&family=Mulish:wght@400;600;700&display=swap" rel="stylesheet">
<style>
:root{
  --blue:#1b5ea8;
  --blue-dark:#174f8c;
  --orange:#f7941d;
  --ink:#444;
  --muted:#666;
  --line:#cfcfcf;
  --band:#f1f1f1;
  --footer:#111;
  --white:#fff;
}
*{box-sizing:border-box;margin:0;padding:0}
html,body{width:1200px;height:3956px;overflow:hidden;background:var(--white)}
body{position:relative;font-family:"Mulish",sans-serif;color:var(--ink)}
.abs{position:absolute}
h2{font-family:"Ubuntu",sans-serif;font-weight:400;color:var(--blue);font-size:42px;text-align:center;position:absolute;left:0;width:1200px}

/* header */
.site-header{position:absolute;top:0;left:0;width:1200px;height:124px;background:var(--white)}
.topbar{position:absolute;top:10px;right:75px;display:flex;gap:40px;font-size:13px;color:var(--white)}
.topbar span{display:flex;align-items:center;gap:10px}
.topbar-band{position:absolute;top:0;left:720px;width:480px;height:42px;background:var(--blue)}
.brand{position:absolute;left:79px;top:58px;display:flex;align-items:center;gap:10px}
.brand-mark{width:30px;height:30px;border-radius:50%;background:var(--orange)}
.brand-name{font-family:"Ubuntu",sans-serif;font-weight:500;font-size:24px;color:var(--blue)}
.nav{position:absolute;top:74px;right:80px;display:flex;gap:28px;font-size:14px;font-weight:600;color:#555}
.nav .active{color:var(--blue)}

/* hero */
.hero{position:absolute;top:124px;left:0;width:1200px;height:554px;background:linear-gradient(180deg,#1f4fae 0%,#3b8ee0 45%,#f0b46a 78%,#233552 100%)}
.hero-badge{position:absolute;left:751px;top:245px;width:370px;height:370px;border-radius:50%;background:var(--orange);color:var(--white);text-align:center;padding:68px 36px 0}
.hero-badge h1{font-family:"Ubuntu",sans-serif;font-weight:400;font-size:34px;line-height:42px}
.hero-badge p{font-size:16px;line-height:26px;margin-top:14px}
.hero-next{position:absolute;left:1049px;top:496px;width:52px;height:52px;border-radius:50%;background:#333}

/* features */
.feature{position:absolute;top:757px;width:254px;height:343px;background:var(--white);box-shadow:0 4px 14px rgba(0,0,0,.18);text-align:center;padding:45px 20px 0}
.feature-icon{width:96px;height:96px;border-radius:50%;background:var(--orange);margin:0 auto;display:flex;align-items:center;justify-content:center}
.feature h3{font-family:"Ubuntu",sans-serif;font-weight:400;font-size:19px;color:#333;margin-top:38px}
.feature p{font-size:13.5px;line-height:26px;color:var(--muted);margin-top:16px}

/* welcome */
.welcome-text{position:absolute;left:205px;width:790px;top:1240px;text-align:center;font-size:14px;line-height:26px;color:var(--muted)}
.welcome-text p+p{margin-top:14px}
.btn{position:absolute;height:50px;border-radius:25px;background:var(--blue-dark);color:var(--white);font-size:15px;font-weight:700;display:flex;align-items:center;justify-content:center;letter-spacing:.3px}

/* testimonials */
.band{position:absolute;left:0;width:1200px;background:var(--band)}
.testimonial{position:absolute;top:1722px;width:470px}
.avatar{position:absolute;left:0;top:0;width:90px;height:90px;border-radius:50%;background:linear-gradient(160deg,#c9d3de,#6d7b8c);border:3px solid var(--white)}
.t-name{position:absolute;left:117px;top:24px;font-size:15px;font-weight:700;color:var(--blue)}
.t-company{position:absolute;left:117px;top:52px;font-size:14px;color:var(--muted)}
.t-text{position:absolute;left:0;top:120px;width:470px;font-size:14px;line-height:26px;color:var(--muted)}

/* blog */
.blog-intro{position:absolute;left:250px;width:700px;top:2102px;text-align:center;font-size:14px;line-height:26px;color:var(--muted)}
.blog-card{position:absolute;background:var(--white);box-shadow:0 2px 10px rgba(0,0,0,.15);overflow:hidden;text-align:center}
.blog-card .photo{width:100%}
.blog-card h4{font-family:"Ubuntu",sans-serif;font-weight:400;font-size:19px;color:#333;white-space:nowrap}
.blog-card p{font-size:13.5px;line-height:25px;color:var(--muted)}
.side h4,.side p{text-align:left;padding:0 22px}
.round-arrow{position:absolute;width:46px;height:46px;border-radius:50%;background:var(--orange);display:flex;align-items:center;justify-content:center}

/* clients */
.clients-title{position:absolute;left:0;width:1200px;top:2940px;text-align:center;font-family:"Ubuntu",sans-serif;font-size:27px;line-height:42px;color:#333}
.pill{position:absolute;height:48px;border:1.5px solid var(--line);border-radius:24px;background:#f6f6f6;display:flex;align-items:center;justify-content:center;font-size:16px;color:#444}

/* contact */
.field{position:absolute;width:330px;border-bottom:1px solid var(--line);font-size:14px;color:#555;padding-bottom:16px}
.info{position:absolute;left:830px;display:flex;gap:22px;font-size:14px;line-height:22px;color:#555;align-items:flex-start}

.site-footer{position:absolute;left:0;top:3895px;width:1200px;height:61px;background:var(--footer);color:#aaa;font-size:13px;display:flex;align-items:center;justify-content:center}
</style>
</head>
<body>

<header class="site-header">
  <div class="topbar-band"></div>
  <div class="topbar">
    <span><svg width="16" height="16" viewBox="0 0 24 24"><path d="M6 2l4 5-2 3c1 3 3 5 6 6l3-2 5 4-3 4C10 22 2 14 2 5z" fill="#fff"/></svg>800-555-0142</span>
    <span><svg width="18" height="14" viewBox="0 0 18 14"><rect x="0" y="0" width="18" height="14" fill="#fff"/><path d="M0 0l9 7 9-7" stroke="#1b5ea8" stroke-width="1.5" fill="none"/></svg>support@qolvarenergy.com</span>
  </div>
  <div class="brand"><div class="brand-mark"></div><div class="brand-name">QOLVAR ENERGY</div></div>
  <nav class="nav"><span class="active">HOME</span><span>WHAT WE DO</span><span>ABOUT QVR</span><span>BLOG</span><span>CONTACT</span></nav>
</header>

<section class="hero" role="img" aria-label="City skyline of glass towers at dusk by the waterfront"></section>
<div class="hero-badge">
  <h1>QOLVAR ENERGY<br>INFORMATION</h1>
  <p>QVR provides the technology to efficiently transfer information electronically and access, integrate and manage data.</p>
</div>
<div class="hero-next"><svg width="52" height="52" viewBox="0 0 52 52"><path d="M18 26h16M28 19l7 7-7 7" stroke="#fff" stroke-width="3" fill="none"/></svg></div>

<article class="feature" style="left:79px">
  <div class="feature-icon"><svg width="46" height="46" viewBox="0 0 46 46" fill="none" stroke="#fff" stroke-width="2.5"><rect x="4" y="4" width="18" height="24"/><rect x="24" y="18" width="18" height="24"/><path d="M8 34c0 4 4 6 10 6M38 12c0-4-4-6-10-6"/></svg></div>
  <h3>Exchange Solutions</h3>
  <p>Our platform for partner reports, logs, surveys and countless other documents, allows you to outsource time consuming support to QVR.</p>
</article>
<article class="feature" style="left:341px">
  <div class="feature-icon"><svg width="46" height="46" viewBox="0 0 46 46" fill="none" stroke="#fff" stroke-width="2.5"><rect x="4" y="6" width="32" height="8"/><rect x="4" y="18" width="32" height="8"/><rect x="4" y="30" width="24" height="8"/><circle cx="36" cy="36" r="6"/></svg></div>
  <h3>Data Management</h3>
  <p>Our data management solutions make it easier for your company to track and manage production and other mission critical business data.</p>
</article>
<article class="feature" style="left:603px">
  <div class="feature-icon"><svg width="46" height="46" viewBox="0 0 46 46" fill="none" stroke="#fff" stroke-width="2.5"><path d="M3 18l10-8 10 6 10-6 10 8M8 22l12 12 4-2 4 2 10-12"/></svg></div>
  <h3>Owner Relationship</h3>
  <p>With over 85 companies, QVR operates the largest network of internet owner portals in the industry.</p>
</article>
<article class="feature" style="left:865px">
  <div class="feature-icon"><svg width="46" height="46" viewBox="0 0 46 46" fill="none" stroke="#fff" stroke-width="2.5"><circle cx="23" cy="23" r="19"/><path d="M23 20v13"/><circle cx="23" cy="14" r="1.5" fill="#fff"/></svg></div>
  <h3>About QVR</h3>
  <p>Qolvar Energy Information has been providing electronic exchange solutions for the energy industry for over 20 years.</p>
</article>

<h2 style="top:1172px">Welcome to QVR</h2>
<div class="welcome-text">
  <p>Qolvar Energy Information has been providing electronic exchange solutions for the energy industry for over 20 years. QVR utilizes proven data integration techniques to provide customers with cost effective methods to efficiently access, transform and distribute their data. Our customer list includes over 95% of the Meridian 500 energy companies.</p>
  <p>Our company was founded in 1991, and established itself as the sole provider of audited crude oil pricing data to the oil industry. In 1996, partnered with Halvorne and Kestrel Oil, QVR developed the on-line pipeline tariff analysis system, RateLedger, along with integration software that allows customers to seamlessly integrate tariff data into their trading, accounting, and marketing systems.</p>
</div>
<div class="btn" style="left:409px;top:1462px;width:184px">KNOW MORE</div>
<div class="btn" style="left:606px;top:1462px;width:186px">CONTACT US</div>

<section class="band" style="top:1608px;height:383px"></section>
<h2 style="top:1652px">Testimonials</h2>
<div class="testimonial" style="left:80px">
  <div class="avatar" role="img" aria-label="Portrait photo of the client"></div>
  <div class="t-name">NAME SURNAME</div><div class="t-company">Company name</div>
  <p class="t-text">Lorem Ipsum is simply dummy text of the printing and typesetting industry. Lorem Ipsum has been the industry's standard dummy text ever since the 1500s, when an unknown printer took a galley of type and scrambled.</p>
</div>
<div class="testimonial" style="left:625px">
  <div class="avatar" role="img" aria-label="Portrait photo of the client"></div>
  <div class="t-name">NAME SURNAME</div><div class="t-company">Company name</div>
  <p class="t-text">Lorem Ipsum is simply dummy text of the printing and typesetting industry. Lorem Ipsum has been the industry's standard dummy text ever since the 1500s, when an unknown printer took a galley of type and scrambled.</p>
</div>

<h2 style="top:2030px">Latest Blog</h2>
<p class="blog-intro">Lorem Ipsum is simply dummy text of the printing and typesetting industry. Lorem Ipsum has been the industry's standard dummy text ever since the 1500s, when an unknown.</p>
<svg class="abs" style="left:370px;top:2180px" width="460" height="44" viewBox="0 0 460 44">
  <line x1="40" y1="22" x2="205" y2="22" stroke="#f7941d" stroke-width="1.5"/>
  <line x1="255" y1="22" x2="420" y2="22" stroke="#f7941d" stroke-width="1.5"/>
  <rect x="18" y="6" width="32" height="32" rx="4" fill="#f7941d" opacity=".35"/><rect x="22" y="10" width="24" height="24" rx="3" fill="#f7941d"/>
  <rect x="210" y="6" width="32" height="32" rx="4" fill="#f7941d" opacity=".35"/><rect x="214" y="10" width="24" height="24" rx="3" fill="#f7941d"/>
  <path d="M226 15l2.5 5 5.5.6-4 3.8 1 5.4-5-2.7-5 2.7 1-5.4-4-3.8 5.5-.6z" fill="none" stroke="#fff" stroke-width="1.3"/>
  <rect x="410" y="6" width="32" height="32" rx="4" fill="#f7941d" opacity=".35"/><rect x="414" y="10" width="24" height="24" rx="3" fill="#f7941d"/>
</svg>
<div class="abs" style="left:0;width:1200px;top:2255px;text-align:center;font-size:19px;color:#555">Oct 22</div>

<article class="blog-card side" style="left:190px;top:2339px;width:240px;height:417px">
  <div class="photo" role="img" aria-label="Photo of colleagues working together at a laptop" style="height:219px;background:linear-gradient(150deg,#d9c2a6,#8a6f57)"></div>
  <h4 style="margin-top:34px">Lorem Ipsum is simply</h4>
  <p style="margin-top:14px">Lorem Ipsum is simply dummy text of the printing and typesetting industry. Lorem Ipsum has been the industry's standard.</p>
</article>
<article class="blog-card side" style="left:770px;top:2339px;width:250px;height:417px">
  <div class="photo" role="img" aria-label="Photo of an industrial plant lit at dusk" style="height:219px;background:linear-gradient(180deg,#4e68a8,#b47d6a 70%,#2b2f45)"></div>
  <h4 style="margin-top:34px;padding-left:40px">Lorem Ipsum is simply</h4>
  <p style="margin-top:14px;padding-left:40px">Lorem Ipsum is simply dummy text of the printing and typesetting industry. Lorem Ipsum has been the industry's standard.</p>
</article>
<article class="blog-card" style="left:427px;top:2307px;width:346px;height:484px;border-radius:6px;box-shadow:0 4px 18px rgba(0,0,0,.25)">
  <div class="photo" role="img" aria-label="Photo of hands typing on a laptop keyboard" style="height:238px;background:linear-gradient(160deg,#a9c4dc,#4f6f8e)"></div>
  <h4 style="margin-top:32px">Lorem Ipsum is simply dummy.</h4>
  <p style="margin:16px 30px 0">Lorem Ipsum is simply dummy text of the printing and typesetting industry. Lorem Ipsum has been the industry's standard dummy text</p>
  <div style="margin-top:22px;font-size:12px;color:var(--orange);letter-spacing:.5px">READ MORE</div>
</article>
<div class="round-arrow" style="left:577px;top:2764px;width:50px;height:50px"><svg width="22" height="22" viewBox="0 0 22 22"><path d="M4 11h13M12 5l6 6-6 6" stroke="#fff" stroke-width="2.5" fill="none"/></svg></div>
<div class="round-arrow" style="left:77px;top:2535px"><svg width="20" height="20" viewBox="0 0 20 20"><path d="M13 4l-6 6 6 6" stroke="#fff" stroke-width="2.5" fill="none"/></svg></div>
<div class="round-arrow" style="left:1077px;top:2535px"><svg width="20" height="20" viewBox="0 0 20 20"><path d="M7 4l6 6-6 6" stroke="#fff" stroke-width="2.5" fill="none"/></svg></div>

<section class="band" style="top:2893px;height:496px"></section>
<div class="clients-title">Want to see what Qolvar Energy can do for your company?<br>Visit some of our client-branded customer and owner relations websites</div>
<div class="pill" style="left:264px;top:3048px;width:124px">Corvane</div>
<div class="pill" style="left:398px;top:3048px;width:203px">Brisella</div>
<div class="pill" style="left:614px;top:3048px;width:322px">Tamberly Resources</div>
<div class="pill" style="left:190px;top:3111px;width:372px">Westmarch Resources</div>
<div class="pill" style="left:583px;top:3111px;width:424px">Ridgeplain Resources</div>
<div class="pill" style="left:103px;top:3174px;width:337px">Oakhollow</div>
<div class="pill" style="left:456px;top:3174px;width:243px">Silvercrag</div>
<div class="pill" style="left:717px;top:3174px;width:380px">Norvik Ashford</div>
<div class="btn" style="left:496px;top:3262px;width:208px">EXPLORE MORE</div>

<h2 style="top:3435px">Contact us</h2>
<div class="field" style="left:79px;top:3518px;padding-left:16px">Your Name</div>
<div class="field" style="left:445px;top:3518px;padding-left:16px">Your E-Mail</div>
<div class="field" style="left:79px;top:3581px;padding-left:16px">Your Phone</div>
<div class="field" style="left:445px;top:3581px;padding-left:16px">Subject</div>
<div class="field" style="left:79px;top:3644px;width:696px;height:78px;padding-left:16px">Message</div>
<div class="btn" style="left:330px;top:3755px;width:184px">SEND</div>

<div class="info" style="top:3562px"><svg width="26" height="24" viewBox="0 0 24 24"><path d="M6 2l4 5-2 3c1 3 3 5 6 6l3-2 5 4-3 4C10 22 2 14 2 5z" fill="none" stroke="#1b5ea8" stroke-width="1.6"/></svg><span>1300 555 014</span></div>
<div class="info" style="top:3610px"><svg width="26" height="20" viewBox="0 0 26 20"><rect x="1" y="1" width="24" height="18" fill="none" stroke="#1b5ea8" stroke-width="1.6"/><path d="M1 1l12 10 12-10" fill="none" stroke="#1b5ea8" stroke-width="1.6"/></svg><span>hello@qolvarenergy.com</span></div>
<div class="info" style="top:3658px"><svg width="26" height="30" viewBox="0 0 26 30"><path d="M13 28C5 18 3 14 3 10a10 10 0 0120 0c0 4-2 8-10 18z" fill="none" stroke="#1b5ea8" stroke-width="1.6"/><circle cx="13" cy="10" r="3.5" fill="none" stroke="#1b5ea8" stroke-width="1.6"/></svg><span>410 Larkspur Ave, Suite 200<br>Fernvale, TX 70000</span></div>

<footer class="site-footer">2018 © QOLVARENERGY - All Rights Reserved</footer>

</body>
</html>
```